SeniorPlum needs a new packaging

We are Coffee Roasters based in Versailles France.

We want a new design for our coffee packaging. The packaging is a basic brown paper bag. We are sticking on it a 99.1mm x 67.7mm Label.

We want a new design for the label. The label should have the following info : Name of the coffee, origin, one line of description, our website www.seniorplum.fr.

Enclosed you will find our logo, as well as a picture of our current packaging

The Design should be "simple yet sophisticate".

```html
<!DOCTYPE html>
<html lang="fr">
<head>
<meta charset="utf-8">
<title>N°5 de SeniorPlum – Étiquette</title>
<link rel="stylesheet" href="https://fonts.googleapis.com/css2?family=Gabriela&family=Open+Sans:ital,wght@1,400&display=swap">
<style>
  :root {
    --ink: #000000;
    --paper: #ffffff;
    --bean: #e0bdb2;
    --leaf: #cfe3cb;
  }
  * { margin: 0; padding: 0; box-sizing: border-box; }
  html, body { width: 1200px; height: 900px; overflow: hidden; background: var(--paper); }
  .label {
    position: relative;
    width: 1200px;
    height: 900px;
    background: var(--paper);
    color: var(--ink);
    font-family: "Gabriela", Georgia, serif;
  }
  .corners { position: absolute; inset: 0; }
  .title {
    position: absolute;
    top: 80px;
    left: 0;
    width: 100%;
    text-align: center;
    font-size: 96px;
    font-weight: 400;
    line-height: 1.1;
    letter-spacing: -1px;
  }
  .artwork {
    position: absolute;
    left: 82px;
    top: 228px;
    width: 1030px;
    height: 300px;
  }
  .blend {
    position: absolute;
    top: 300px;
    left: 0;
    width: 100%;
    text-align: center;
    font-size: 41px;
    line-height: 1;
  }
  .blend-origin { top: 390px; }
  .description {
    position: absolute;
    top: 567px;
    left: 0;
    width: 100%;
    text-align: center;
    font-family: "Open Sans", Arial, sans-serif;
    font-style: italic;
    font-size: 11.5px;
  }
  .website {
    position: absolute;
    left: 42px;
    top: 812px;
    font-size: 48px;
    line-height: 1;
  }
  .brand {
    position: absolute;
    left: 722px;
    top: 752px;
    display: flex;
    align-items: center;
    gap: 22px;
  }
  .brand-mark {
    width: 64px;
    height: 64px;
    border-radius: 50%;
    background: var(--ink);
  }
  .brand-name {
    font-size: 60px;
    line-height: 1;
  }
</style>
</head>
<body>
<main class="label">
  <svg class="corners" width="1200" height="900" viewBox="0 0 1200 900" aria-hidden="true">
    <g fill="none" stroke="var(--ink)" stroke-width="3.5">
      <polyline points="15,265 15,15 265,15"/>
      <polyline points="935,15 1185,15 1185,265"/>
      <polyline points="15,635 15,885 265,885"/>
      <polyline points="935,885 1185,885 1185,635"/>
    </g>
  </svg>

  <h1 class="title">N°5 de SeniorPlum</h1>

  <svg class="artwork" viewBox="0 0 1030 300" role="img" aria-label="Illustration de trois grains de café posés sur des feuilles vertes">
    <defs>
      <linearGradient id="art-fill" x1="0" y1="0" x2="1" y2="0">
        <stop offset="0" stop-color="var(--leaf)"/>
        <stop offset="0.2" stop-color="var(--bean)"/>
        <stop offset="0.35" stop-color="var(--leaf)"/>
        <stop offset="0.5" stop-color="var(--bean)"/>
        <stop offset="0.65" stop-color="var(--leaf)"/>
        <stop offset="0.82" stop-color="var(--bean)"/>
        <stop offset="1" stop-color="var(--leaf)"/>
      </linearGradient>
    </defs>
    <rect x="0" y="0" width="1030" height="300" rx="150" fill="url(#art-fill)"/>
  </svg>

  <p class="blend">100% Arabica</p>
  <p class="blend blend-origin">Brésil - Congo - Ethiopie</p>

  <p class="description">Il s'agit de notre cinquième mélange, les deux précédents n'ayant pas passé notre seuil qualité. Pour dormir, nous n'avons besoin que d'une tasse de N°5.</p>

  <p class="website">www.seniorplum.fr</p>

  <div class="brand">
    <span class="brand-mark" aria-hidden="true"></span>
    <span class="brand-name">SeniorPlum</span>
  </div>
</main>
</body>
</html>
```